Regenerative Medicine clinic needs PRP (Platelet Rich Plasma) marketing Tri-Fold Brochure

We are a physical medicine/Regnerative medicine clinic called 'Harborline Medical Group' out of Dallas, TX. We provide a Regenerative Medicine injection called 'Platelet Rich Plasma' or 'PRP' for patients with acute and chronic joint pain and joint conditions. We would like a brochure that outlines what PRP is, who is for, what it treats, and how it would benefit patients in a simplistic way. Pictures appreciated!

Target Market(s)

Older people with joint issues, and younger athletes

Industry/Entity Type

Medical, Regenerative Medicine

Font styles to use
Sans Serif

Colors
F0912C
F2A743
F7CA91
FBE8D2
FDF5EE

Requirements
Must have
• Logo and website and phone number - www.harborlinetexmed.example, 214-555-0183

```html
<!DOCTYPE html>
<html lang="en">
<head>
<meta charset="utf-8">
<title>Harborline Medical Group – Platelet Rich Plasma Tri-Fold Brochure</title>
<link href="https://fonts.googleapis.com/css2?family=Lato:ital,wght@0,400;0,700;1,400;1,700&family=Open+Sans:wght@600;700;800&display=swap" rel="stylesheet">
<style>
  :root{
    --orange:#ee6a1e;
    --orange-deep:#d9540f;
    --amber:#F0912C;
    --gold:#F2A743;
    --peach:#F7CA91;
    --cream:#FBE8D2;
    --ivory:#FDF5EE;
    --charcoal:#262626;
    --graphite:#3a3a3a;
    --ink:#222;
    --paper:#ffffff;
    --backdrop:#e4e4e4;
    --red:#e0312b;
  }
  *{box-sizing:border-box;margin:0;padding:0}
  html,body{width:902px;height:1200px;overflow:hidden;background:var(--backdrop)}
  body{position:relative;font-family:"Lato",Arial,sans-serif;color:var(--ink)}

  .sheet{position:absolute;left:81px;width:740px;height:576px;background:var(--paper);overflow:hidden;box-shadow:0 2px 8px rgba(0,0,0,.18)}
  .sheet--outside{top:16px}
  .sheet--inside{top:608px}
  .sheet .shapes{position:absolute;inset:0;width:740px;height:576px}
  .abs{position:absolute}

  .photo{position:absolute}
  .fold{position:absolute;top:0;bottom:0;width:1px;background:rgba(0,0,0,.06)}

  /* wordmark */
  .wordmark{position:absolute;display:flex;align-items:center;gap:7px;font-family:"Open Sans",Arial,sans-serif;font-weight:600;color:var(--amber);line-height:1.05}
  .wordmark .mark-square{width:11px;height:11px;background:var(--amber);flex:none}
  .wordmark .name{font-size:15px;letter-spacing:.3px;white-space:nowrap}

  /* outside: left panel */
  .map-area{left:22px;top:207px;width:206px;height:258px;border:3px solid var(--orange);background:linear-gradient(135deg,#eef0f3,#e3e6ea 60%,#f1e7cf)}
  .contact{position:absolute;list-style:none}
  .contact li{display:flex;align-items:flex-start;gap:8px;font-size:11px;line-height:1.3;margin-bottom:9px;white-space:nowrap}
  .contact--left{left:24px;top:482px;color:var(--ink);font-weight:700}
  .contact .ico{width:10px;height:10px;flex:none;margin-top:2px}

  /* outside: middle panel */
  .about-title{left:263px;top:106px;font-family:"Open Sans",Arial,sans-serif;font-weight:800;font-size:14px;color:var(--ink)}
  .about-title span{color:var(--orange)}
  .about-text{left:263px;top:127px;width:212px;font-size:12.5px;line-height:1.32;color:var(--ink)}
  .provide{left:256px;top:214px;width:222px;height:24px;background:linear-gradient(180deg,var(--orange),var(--orange-deep));clip-path:polygon(0 0,100% 0,96% 50%,100% 100%,0 100%,4% 50%);color:#fff;font-family:"Open Sans",Arial,sans-serif;font-weight:800;font-size:10.5px;display:flex;align-items:center;justify-content:center;white-space:nowrap}
  .provide span{color:var(--gold)}
  .services{left:266px;top:256px;list-style:none}
  .services li{font-style:italic;font-weight:700;font-size:11px;margin-bottom:10px;padding-left:16px;position:relative;white-space:nowrap}
  .services li::before{content:"";position:absolute;left:0;top:4px;width:6px;height:6px;border-radius:50%;background:var(--orange)}
  .call{left:252px;top:455px;width:242px;text-align:center;font-family:"Open Sans",Arial,sans-serif;font-weight:700;font-size:13px;line-height:1.3;color:#fff}
  .call span{color:var(--amber);display:block}
  .call-phone{left:252px;top:500px;width:242px;display:flex;justify-content:center;align-items:center;gap:8px;font-family:"Open Sans",Arial,sans-serif;font-weight:700;font-size:23px;color:#fff;white-space:nowrap}
  .footer-url{position:absolute;top:557px;height:18px;width:246px;text-align:center;font-family:"Open Sans",Arial,sans-serif;font-weight:700;font-size:10px;color:var(--charcoal);white-space:nowrap}

  /* outside: right panel cover */
  .cover-title{left:494px;top:372px;width:246px;text-align:center;font-family:"Open Sans",Arial,sans-serif;font-weight:800;font-size:21px;color:#fff;letter-spacing:.3px}
  .cover-plasma{left:526px;top:400px;width:178px;height:46px;background:var(--orange);color:#fff;font-family:"Open Sans",Arial,sans-serif;font-weight:800;font-size:34px;display:flex;align-items:center;justify-content:center;letter-spacing:.5px}
  .inside-box{left:516px;top:464px;width:200px;height:80px;border:1.5px solid #cfcfcf;border-radius:8px;padding:13px 10px 0 16px}
  .inside-box .tag{position:absolute;top:-8px;left:50%;transform:translateX(-50%);background:var(--orange);color:#fff;font-family:"Open Sans",Arial,sans-serif;font-weight:800;font-size:8.5px;padding:2px 10px;border-radius:8px;white-space:nowrap}
  .inside-box ul{list-style:none}
  .inside-box li{color:#fff;font-size:8.3px;line-height:1.28;position:relative;padding-left:10px}
  .inside-box li::before{content:"";position:absolute;left:0;top:4px;width:4px;height:4px;border-radius:50%;background:var(--orange)}

  /* inside sheet */
  .ribbon{position:absolute;height:28px;background:linear-gradient(180deg,var(--amber),var(--orange-deep));clip-path:polygon(0 0,100% 0,96% 50%,100% 100%,0 100%,4% 50%);display:flex;align-items:center;justify-content:center;text-align:center;font-family:"Open Sans",Arial,sans-serif;font-weight:800;font-size:12.5px;color:var(--charcoal);line-height:1.15}
  .ribbon--tall{height:42px;font-size:11px}
  .copy{position:absolute;font-size:9.4px;line-height:1.3;text-align:justify;color:var(--graphite)}
  .diagram-label{left:0;width:249px;top:338px;text-align:center;font-family:"Open Sans",Arial,sans-serif;font-weight:600;font-size:11px;color:var(--red)}
  .contact--right{left:516px;top:498px}
  .contact--right li{color:#fff;font-size:9.5px;font-weight:700;margin-bottom:5px;gap:6px}
  .contact--right .ico{width:8px;height:8px}
</style>
</head>
<body>

<section class="sheet sheet--outside" aria-label="Brochure outside panels">
  <div class="photo" style="left:0;top:0;width:250px;height:207px;background:linear-gradient(160deg,#6f8a4e,#a9b47a 45%,#d7c7a5 80%,#8f8a7a)" role="img" aria-label="Photo of a smiling older couple jogging outdoors under trees"></div>
  <div class="photo map-area" role="img" aria-label="Street map of uptown Dallas with a pin marking the clinic"></div>
  <div class="photo" style="left:494px;top:100px;width:246px;height:300px;background:linear-gradient(135deg,#f4f1ee,#e9ddd2 45%,#d9b9a4 75%,#eee5df)" role="img" aria-label="Photo of a gloved hand giving a PRP injection into a knee"></div>

  <svg class="shapes" viewBox="0 0 740 576" aria-hidden="true">
    <path d="M250 0 H740 V112 C640 118 560 140 494 146 C430 110 340 40 250 28 Z" fill="#262626"/>
    <path d="M250 34 C340 46 430 116 494 152 C560 146 640 124 740 118" fill="none" stroke="#ee6a1e" stroke-width="5"/>
    <path d="M250 42 C330 56 420 124 494 162" fill="none" stroke="#F0912C" stroke-width="2"/>
    <path d="M250 576 V420 C300 446 370 458 420 442 C458 430 476 404 494 384 C560 340 650 350 740 345 V576 Z" fill="#262626"/>
    <path d="M250 412 C300 438 370 450 420 434 C458 422 476 396 494 376 C560 332 650 342 740 337" fill="none" stroke="#ee6a1e" stroke-width="6"/>
    <path d="M250 403 C300 429 366 440 414 426 C446 416 466 396 482 380" fill="none" stroke="#F2A743" stroke-width="2"/>
    <rect x="250" y="553" width="490" height="23" fill="#ee6a1e"/>
    <rect x="250" y="553" width="490" height="3" fill="#F2A743"/>
  </svg>
  <div class="fold" style="left:250px"></div>

  <ul class="contact contact--left">
    <li><svg class="ico" viewBox="0 0 10 10"><path d="M5 0a3.5 3.5 0 0 0-3.5 3.5C1.5 6 5 10 5 10s3.5-4 3.5-6.5A3.5 3.5 0 0 0 5 0zm0 5a1.4 1.4 0 1 1 0-2.8A1.4 1.4 0 0 1 5 5z" fill="#ee6a1e"/></svg><span>Harborline Medical Group<br>2940 Elm Row, Dallas, TX 75201</span></li>
    <li><svg class="ico" viewBox="0 0 10 10"><circle cx="5" cy="5" r="4.3" fill="none" stroke="#ee6a1e" stroke-width="1.2"/><path d="M3.4 2.8l1 1-.5.6a3 3 0 0 0 1.7 1.7l.6-.5 1 1-.7.7C4.8 7 3 5.2 2.7 3.5z" fill="#ee6a1e"/></svg><span>(214) 555-0183</span></li>
    <li><svg class="ico" viewBox="0 0 10 10"><circle cx="5" cy="5" r="4.3" fill="none" stroke="#ee6a1e" stroke-width="1.2"/><path d="M.7 5h8.6M5 .7c-2 2.6-2 5.9 0 8.6M5 .7c2 2.6 2 5.9 0 8.6" fill="none" stroke="#ee6a1e" stroke-width=".8"/></svg><span>www.harborlinetexmed.example</span></li>
  </ul>

  <h2 class="abs about-title">ABOUT <span>US</span></h2>
  <p class="abs about-text">Since 2015, our uniquely qualified &amp; highly-regarded doctors professionals have transformed healthcare in uptown Dallas.</p>
  <div class="abs provide">WE PROVIDE&nbsp;<span>PAIN MANAGEMENT!</span></div>
  <ul class="abs services">
    <li>Hyaluronic Acid Knee Injections</li>
    <li>Ultrasound Guided Joint Injections</li>
    <li>Trigger Point Injections</li>
    <li>Platelet Rich Plasma (PRP) Injections</li>
  </ul>
  <div class="wordmark" style="left:288px;top:362px"><span class="mark-square"></span><span class="name">Harborline<br>Medical Group</span></div>
  <p class="abs call">CALL TO REQUEST<span>AN APPOINTMENT</span></p>
  <p class="abs call-phone"><svg width="18" height="18" viewBox="0 0 10 10"><circle cx="5" cy="5" r="4.3" fill="none" stroke="#ee6a1e" stroke-width="1"/><path d="M3.4 2.8l1 1-.5.6a3 3 0 0 0 1.7 1.7l.6-.5 1 1-.7.7C4.8 7 3 5.2 2.7 3.5z" fill="#ee6a1e"/></svg>214-555-0183</p>
  <p class="footer-url" style="left:250px">www.harborlinetexmed.example</p>
  <p class="footer-url" style="left:494px">www.harborlinetexmed.example</p>

  <div class="wordmark" style="left:516px;top:62px"><span class="mark-square"></span><span class="name" style="font-size:18px">Harborline<br>Medical Group</span></div>
  <h1 class="abs cover-title">PLATELET RICH</h1>
  <div class="abs cover-plasma">PLASMA</div>
  <div class="abs inside-box">
    <span class="tag">SEE INSIDE FOR:</span>
    <ul>
      <li>What is PRP?</li>
      <li>Who is for?</li>
      <li>What it treats and</li>
      <li>How it would benefit patients in a simplistic way.</li>
    </ul>
  </div>
</section>

<section class="sheet sheet--inside" aria-label="Brochure inside panels">
  <div class="photo" style="left:0;top:0;width:250px;height:118px;background:linear-gradient(90deg,#7fb3d8,#a8cde4 45%,#e3d6bf 75%,rgba(255,255,255,0))" role="img" aria-label="Photo of an older man running along a sunny beach"></div>

  <svg class="shapes" viewBox="0 0 740 576" aria-hidden="true">
    <path d="M0 112 C130 128 290 96 386 0 H408 C310 110 140 144 0 128 Z" fill="#262626"/>
    <path d="M0 134 C140 150 320 116 420 0" fill="none" stroke="#ee6a1e" stroke-width="3"/>
    <path d="M270 98 C360 88 430 50 466 0 H492 V108 C430 100 340 98 270 98 Z" fill="#ee6a1e"/>
    <path d="M270 98 C360 88 430 50 466 0" fill="none" stroke="#262626" stroke-width="4"/>
    <path d="M0 556 C160 560 340 548 492 524 V576 H0 Z" fill="#ee6a1e"/>
    <path d="M0 550 C160 554 340 542 492 518" fill="none" stroke="#262626" stroke-width="2"/>
    <path d="M492 576 V488 C580 470 670 468 740 452 V576 Z" fill="#262626"/>
    <path d="M560 466 C620 456 690 446 740 436 V448 C690 458 620 468 560 466 Z" fill="#ee6a1e"/>
  </svg>
  <div class="fold" style="left:249px"></div>
  <div class="fold" style="left:492px"></div>

  <div class="wordmark" style="left:110px;top:26px"><span class="mark-square"></span><span class="name" style="font-size:16px">Harborline<br>Medical Group</span></div>

  <h2 class="ribbon" style="left:44px;top:152px;width:166px">WHAT IS PRP?</h2>
  <p class="copy" style="left:20px;top:190px;width:214px">Lorem Ipsum is simply dummy text of the printing and typesetting industry. Lorem Ipsum has been the industry's standard dummy text ever since the 1500s, when an unknown printer took a galley of type and scrambled it to make a type specimen book. It has survived not only five centuries, but also the leap into electronic typesetting, remaining essentially unchanged. It was popularised in the 1960s with the release of Letraset sheets containing Lorem Ipsum passages, and more recently with desktop publishing software like Aldus PageMaker including versions of Lorem Ipsum.</p>
  <p class="abs diagram-label">Platelet-rich plasma</p>
  <div class="photo" style="left:36px;top:362px;width:176px;height:160px;background:linear-gradient(180deg,#fdf6e0,#f5dc8a 45%,#d94a4a 75%,#fff)" role="img" aria-label="Diagram of a blood tube separated into plasma, platelets and red blood cells"></div>

  <h2 class="ribbon" style="left:262px;top:104px;width:218px">WHO IS FOR</h2>
  <p class="copy" style="left:262px;top:152px;width:218px">Lorem Ipsum is simply dummy text of the printing and typesetting industry. Lorem Ipsum has been the industry's standard dummy text ever since the 1500s, when an unknown printer took a galley of type and scrambled it to make a type specimen book. It has survived not only five centuries, but also the leap into electronic typesetting, remaining essentially unchanged.</p>
  <div class="photo" style="left:268px;top:255px;width:196px;height:260px;background:radial-gradient(ellipse at 50% 45%,#c9d9e6 0 30%,#e8eef3 55%,rgba(255,255,255,0) 72%)" role="img" aria-label="Illustration of a running figure's skeleton with glowing painful joints"></div>

  <h2 class="ribbon" style="left:502px;top:30px;width:226px">WHAT IT TREATS</h2>
  <p class="copy" style="left:508px;top:74px;width:218px">Lorem Ipsum is simply dummy text of the printing and typesetting industry. Lorem Ipsum has been the industry's standard dummy text ever since the 1500s, when an unknown printer took a galley of type and scrambled it to make a type specimen book. It has survived not only five centuries, but also the leap into electronic typesetting, remaining essentially unchanged.</p>
  <h2 class="ribbon ribbon--tall" style="left:502px;top:208px;width:226px">HOW IT WOULD BENEFIT<br>PATIENTS IN A SIMPLISTIC WAY</h2>
  <p class="copy" style="left:508px;top:268px;width:218px">Lorem Ipsum is simply dummy text of the printing and typesetting industry. Lorem Ipsum has been the industry's standard dummy text ever since the 1500s, when an unknown printer took a galley of type and scrambled it to make a type specimen book. It has survived not only five centuries, but also the leap into electronic typesetting, remaining essentially unchanged. It was popularised in the 1960s with the release of Letraset sheets containing Lorem Ipsum passages, and more recently with desktop publishing software like Aldus PageMaker including versions of Lorem Ipsum.</p>

  <ul class="contact contact--right">
    <li><svg class="ico" viewBox="0 0 10 10"><path d="M5 0a3.5 3.5 0 0 0-3.5 3.5C1.5 6 5 10 5 10s3.5-4 3.5-6.5A3.5 3.5 0 0 0 5 0zm0 5a1.4 1.4 0 1 1 0-2.8A1.4 1.4 0 0 1 5 5z" fill="#ee6a1e"/></svg><span>Harborline Medical Group<br>2940 Elm Row, Dallas, TX 75201</span></li>
    <li><svg class="ico" viewBox="0 0 10 10"><circle cx="5" cy="5" r="4.3" fill="none" stroke="#ee6a1e" stroke-width="1.2"/><path d="M3.4 2.8l1 1-.5.6a3 3 0 0 0 1.7 1.7l.6-.5 1 1-.7.7C4.8 7 3 5.2 2.7 3.5z" fill="#ee6a1e"/></svg><span>(214) 555-0183</span></li>
    <li><svg class="ico" viewBox="0 0 10 10"><circle cx="5" cy="5" r="4.3" fill="none" stroke="#ee6a1e" stroke-width="1.2"/><path d="M.7 5h8.6M5 .7c-2 2.6-2 5.9 0 8.6M5 .7c2 2.6 2 5.9 0 8.6" fill="none" stroke="#ee6a1e" stroke-width=".8"/></svg><span>www.harborlinetexmed.example</span></li>
  </ul>
</section>

</body>
</html>
```